insert for clam shell / vape cartridge

Brand : Brevor (roman god of fire)
card insert dimensions are 2.5" in width and 3.375" in height
this is a cannabis product. Open to any and all designs. Currently using very generic text. 5/8" on left edge of design will be covered by the cartridge

Target Market(s)

medical cannabis patients

Industry/Entity Type

Product

Logo Text

Brevor

Requirements
Must have
• logo
Nice to have
• "distilled cannabis oil"
• "no pg/vg"
• subtle use of cannabis leaf
Should not have
• no big (prominent) Pot leaves

```html
<!DOCTYPE html>
<html lang="en">
<head>
<meta charset="utf-8">
<title>Brevor Vapor cartridge insert</title>
<link rel="stylesheet" href="https://fonts.googleapis.com/css2?family=Josefin+Sans:wght@300;400;700&display=swap">
<style>
  :root {
    --paper: #ffffff;
    --ember: #5a2214;
    --ink: #1a1a1a;
    --gold-top: #a6883a;
    --gold-bottom: #8a813b;
    --line: #111111;
  }
  * { box-sizing: border-box; margin: 0; padding: 0; }
  html, body {
    width: 1200px; height: 848px; overflow: hidden;
    background: var(--paper);
    font-family: "Josefin Sans", sans-serif;
  }
  .sheet { position: relative; width: 1200px; height: 848px; }

  .insert {
    position: absolute; top: 69px;
    width: 500px; height: 674px;
    border-radius: 36px; overflow: hidden;
  }
  .insert--light { left: 53px; background: var(--paper); border: 2px solid var(--line); }
  .insert--dark { left: 649px; background: var(--ember); color: var(--paper); }

  .cartridge-zone {
    position: absolute; top: 0; left: 0; width: 162px; height: 100%;
    background: linear-gradient(180deg, var(--gold-top), var(--gold-bottom) 45%, var(--gold-bottom));
  }
  .cartridge-slot {
    position: absolute; top: 37px; left: 27px;
    width: 113px; height: 614px;
    border: 2px solid var(--line); border-radius: 40px;
  }
  .insert--dark .cartridge-slot { top: 39px; left: 28px; }

  .batch {
    position: absolute; top: 521px; left: 152px;
    writing-mode: vertical-rl;
    font-size: 13px; font-weight: 400; letter-spacing: 0.3px;
    color: var(--ink);
  }
  .insert--dark .batch { left: 170px; color: var(--ink); }

  .mark {
    position: absolute; top: 42px; right: 74px;
    width: 124px; height: 124px; border-radius: 50%;
    border: 3px solid var(--ember);
  }
  .insert--dark .mark { border-color: var(--paper); }

  .label { position: absolute; right: 46px; text-align: right; white-space: nowrap; line-height: 1; }
  .insert--light .label { color: var(--ember); }
  .insert--dark .label { color: var(--paper); }

  .brand-name { top: 210px; font-size: 68px; font-weight: 700; letter-spacing: 0.5px; }
  .brand-line { top: 276px; font-size: 52px; font-weight: 300; letter-spacing: 1px; }
  .product-type { top: 336px; font-size: 24px; font-weight: 300; }
  .insert--light .product-type { color: var(--ink); }

  .weight { top: 522px; font-size: 41px; font-weight: 700; }
  .potency { top: 573px; font-size: 13px; font-weight: 400; }
  .free-from { top: 610px; font-size: 21px; font-weight: 400; }
  .insert--light .potency, .insert--light .free-from { color: var(--ink); }
</style>
</head>
<body>
<main class="sheet">

  <section class="insert insert--light" aria-label="Light insert">
    <div class="cartridge-slot"></div>
    <p class="batch">BATCH: 10301701</p>
    <div class="mark"></div>
    <h1 class="label brand-name">BREVOR</h1>
    <p class="label brand-line">VAPOR</p>
    <p class="label product-type">distilled cannabis oil</p>
    <p class="label weight">1 GRAM</p>
    <p class="label potency">THC 70.3%</p>
    <p class="label free-from">No PG or VG</p>
  </section>

  <section class="insert insert--dark" aria-label="Dark insert">
    <div class="cartridge-zone"></div>
    <div class="cartridge-slot"></div>
    <p class="batch">BATCH: 10301701</p>
    <div class="mark"></div>
    <h2 class="label brand-name">BREVOR</h2>
    <p class="label brand-line">VAPOR</p>
    <p class="label product-type">distilled cannabis oil</p>
    <p class="label weight">1 GRAM</p>
    <p class="label potency">THC 70.3%</p>
    <p class="label free-from">No PG or VG</p>
  </section>

</main>
</body>
</html>
```